Exclusive Offer Verbalis December 2022

A design that includes the company logo company and the text set out below. It could be a season design (winter design). it is a short promo to be sent by email. It should express that the promotion is on translation services.

Title: ESPECIAL DICIEMBRE

Information:

10% Descuento del 13 al 16 de diciembre
8% Después del 13 y hasta el 24 de diciembre

En contenidos web, materiales publicitarios, catàlogos, textos legales, manuales y más.

+30 años de experiencia, ISO 17100, traductores nativos

Target Market(s)

B2B Spain - any company that needs translation services

Industry/Entity Type

Services and Translation

Requirements
Must have
• Please take into account our corporate style guide attached
Nice to have
• A design that suggests a special offer from a serious, professional, technological and solid translation company.
Should not have
• Typical Christmas stationery, colours that don't fit into our company design trend.

```html
<!DOCTYPE html>
<html lang="es">
<head>
<meta charset="utf-8">
<title>Especial Diciembre · Verbalis</title>
<link rel="stylesheet" href="https://fonts.googleapis.com/css2?family=Montserrat:wght@600;700;800;900&family=Playfair+Display:wght@500&display=swap">
<style>
  :root {
    --navy: #00305c;
    --snow: #ffffff;
    --gold-dark: #c17a1c;
    --gold-mid: #e2b04e;
    --gold-light: #ffe585;
    --gold-warm: #f7c556;
    --brand-blue: #0060a8;
    --frost: #8fa6bf;
  }
  * { margin: 0; padding: 0; box-sizing: border-box; }
  html, body { width: 960px; height: 1200px; overflow: hidden; background: var(--snow); }
  .promo {
    position: relative;
    width: 960px;
    height: 1200px;
    background: var(--navy);
    overflow: hidden;
    font-family: "Montserrat", Arial, sans-serif;
  }
  .scene { position: absolute; inset: 0; width: 960px; height: 1200px; }
  .foliage {
    position: absolute;
    left: 41px; top: 41px;
    width: 878px; height: 215px;
    background:
      radial-gradient(ellipse at 12% 30%, rgba(226,176,78,0.55), transparent 45%),
      radial-gradient(ellipse at 50% 55%, rgba(255,229,133,0.45), transparent 40%),
      radial-gradient(ellipse at 85% 40%, rgba(247,197,86,0.5), transparent 45%),
      radial-gradient(ellipse at 70% 20%, rgba(143,166,191,0.3), transparent 35%);
  }
  .headline {
    position: absolute;
    left: 0; width: 960px;
    text-align: center;
    font-family: "Playfair Display", Georgia, serif;
    font-weight: 500;
    line-height: 1;
    background: linear-gradient(90deg, var(--gold-dark) 0%, var(--gold-mid) 25%, var(--gold-light) 55%, var(--gold-warm) 85%);
    -webkit-background-clip: text;
    background-clip: text;
    color: transparent;
  }
  .headline--top { top: 282px; font-size: 106px; letter-spacing: 4px; }
  .headline--bottom { top: 393px; font-size: 106px; letter-spacing: 3px; }
  .badge-label {
    position: absolute;
    color: var(--navy);
    text-align: center;
    line-height: 1;
  }
  .badge-label .rate {
    display: block;
    font-weight: 900;
    font-size: 88px;
    letter-spacing: -5px;
  }
  .badge-label .word {
    display: block;
    font-weight: 900;
    font-size: 20px;
    letter-spacing: -0.3px;
    margin-top: 6px;
  }
  .badge-label--ten { left: 64px; top: 540px; width: 152px; }
  .badge-label--eight { left: 756px; top: 672px; width: 146px; }
  .dates {
    position: absolute;
    color: var(--snow);
    font-weight: 700;
    font-size: 25px;
    line-height: 31px;
    text-transform: uppercase;
  }
  .dates--first { left: 276px; top: 558px; }
  .dates--second { right: 281px; top: 676px; text-align: right; }
  .services {
    position: absolute;
    left: 0; width: 960px;
    top: 832px;
    text-align: center;
    color: var(--snow);
    font-weight: 600;
    font-size: 24.5px;
    line-height: 34px;
  }
  .brand-name {
    position: absolute;
    left: 196px; top: 1047px;
    width: 146px;
    text-align: center;
    color: var(--brand-blue);
    font-weight: 800;
    font-size: 30px;
    line-height: 40px;
  }
  .credentials {
    position: absolute;
    left: 362px; top: 1058px;
    color: var(--navy);
    font-weight: 700;
    font-size: 20.5px;
    line-height: 28px;
    text-transform: uppercase;
  }
</style>
</head>
<body>
<main class="promo">
  <svg class="scene" viewBox="0 0 960 1200" aria-hidden="true">
    <defs>
      <linearGradient id="goldLeft" x1="0" x2="1" y1="0" y2="0">
        <stop offset="0" stop-color="#c17a1c"/>
        <stop offset="0.45" stop-color="#ffe585"/>
        <stop offset="1" stop-color="#f7c556"/>
      </linearGradient>
      <linearGradient id="goldRight" x1="1" x2="0" y1="0" y2="0">
        <stop offset="0" stop-color="#c17a1c"/>
        <stop offset="0.45" stop-color="#ffe585"/>
        <stop offset="1" stop-color="#f7c556"/>
      </linearGradient>
      <linearGradient id="goldFrame" x1="0" x2="1" y1="1" y2="0">
        <stop offset="0" stop-color="#c17a1c"/>
        <stop offset="0.5" stop-color="#ffe585"/>
        <stop offset="1" stop-color="#e2b04e"/>
      </linearGradient>
    </defs>
    <path class="snow-hill" d="M0 933 C 230 936, 430 970, 543 1032 C 700 1010, 850 1000, 960 1002 L960 1200 L0 1200 Z" fill="#ffffff"/>
    <polygon class="offer-ribbon" points="40,515 220,515 267,590 220,665 40,665" fill="url(#goldLeft)"/>
    <polygon class="offer-ribbon" points="920,647 741,647 693,722 741,797 920,797" fill="url(#goldRight)"/>
    <rect class="gold-frame" x="40" y="40" width="880" height="1120" fill="none" stroke="url(#goldFrame)" stroke-width="1.6"/>
    <g class="trees" fill="#ffffff">
      <rect x="60" y="824" width="103" height="114" rx="4" role="img" aria-label="Pino nevado"/>
      <rect x="523" y="943" width="78" height="87" rx="4" role="img" aria-label="Pino nevado"/>
      <rect x="746" y="938" width="61" height="67" rx="4" role="img" aria-label="Pino nevado"/>
      <rect x="814" y="893" width="99" height="109" rx="4" role="img" aria-label="Pino nevado"/>
    </g>
  </svg>

  <div class="foliage" role="img" aria-label="Hojas doradas y estrellas de invierno"></div>

  <h1>
    <span class="headline headline--top">ESPECIAL</span>
    <span class="headline headline--bottom">DICIEMBRE</span>
  </h1>

  <div class="badge-label badge-label--ten"><span class="rate">10%</span><span class="word">DESCUENTO</span></div>
  <p class="dates dates--first">Del 13 al<br>16 de diciembre</p>

  <p class="dates dates--second">Después del 13 y<br>hasta el 24<br>de diciembre</p>
  <div class="badge-label badge-label--eight"><span class="rate">8%</span><span class="word">DESCUENTO</span></div>

  <p class="services">En contenidos web, materiales publicitarios,<br>catàlogos, textos legales, manuales y más.</p>

  <div class="brand-name">Verbalis</div>
  <p class="credentials">+30 años de experiencia,<br>ISO 17100, traductores nativos</p>
</main>
</body>
</html>
```